Responsive Website Design for New Social Site (Building User Account)

Brellomar.com is a website that allows people to create preformatted emails to be sent out at a later date. The purpose is to allow people to communicate in the event of an accident or death. The beta site is built but not consumable by the public. It needs a new look before we go live.

I’m speaking specifically about the user account. They are admin tools for creating and publishing communications. They include workflow design, document/message storage, and a dashboard.

I currently have a basic design. Now I’m looking for an inspired design. Something interesting and memorable. Something that draws people in. I have a PPT that can provide guidance on what elements need to be on each page but I’m looking for someone who knows how to create engaging websites.

SCOPE OF EFFORT
There are approximately 23 pages to the website but only 5 distinct page appearances
• Dashboard
• Workflow
• Document/Message/Contact Management
• Education Search
• Account Form
I need a few pop-up designs
• Yes/No/Continue
I need a responsive design (3 sizes)

ARTISTIC QUALITIES
Easy to Use/Understand
New/Inventive/Cool/Memorable
Works with the Logo
Consistent Elements (buttons, text, use of color, etc)

TECHNICAL ASPECTS
I’d like the work provided in a storyboard and individual files for development

PHASES
1. Initial Concept
a. 2-3 Designs Ideas. Just the Dashboard and Workflow in responsive formats
2. Build
a. Create all the pages
b. Provide in storyboard in responsive formats
c. 2 Rounds of Revision
3. Final
a. Provide Storyboard and Files

I'd like to see a portfolio of your responsive web design, especially any user accounts you have created. I've attached three of the initial pages. I'd like to see a concept of what you would produce for at least one of the pages.

Thank you for your interest.

```html
<!DOCTYPE html>
<html lang="en">
<head>
<meta charset="utf-8">
<title>Brellomar – Learning Center</title>
<link href="https://fonts.googleapis.com/css2?family=Arimo:wght@400;700&display=swap" rel="stylesheet">
<style>
:root{
  --page-left:#dcf3cf;
  --page-right:#d7e6ee;
  --header-bg:#cfdeef;
  --user-bg:#b7d98e;
  --sidebar-bg:#4b4b4d;
  --content-bg:#eef0f6;
  --nav-text:#ffffff;
  --nav-active:#f2a98c;
  --link:#8a78e6;
  --title:#ec5a1e;
  --pill:#2f92d8;
  --pill-shadow:#1f6ca6;
  --green-title:#3d9b2c;
  --icon-fill:#e3f3d2;
  --icon-line:#4a6fa5;
  --divider:#b8db95;
  --stat:#f2b9a9;
  --stat-text:#555555;
  --active-bar:#67b23c;
  --end:#f2241c;
  --start:#5aa83a;
  --plan-live:#e23a1c;
  --plan:#8a78e6;
  --text:#333333;
  --muted:#666666;
}
*{box-sizing:border-box;margin:0;padding:0}
html,body{width:1200px;height:869px;overflow:hidden}
body{
  font-family:"Arimo",Arial,sans-serif;
  background:linear-gradient(90deg,var(--page-left),#eef4ea 50%,var(--page-right));
  color:var(--text);
}
.app{position:absolute;left:205px;top:0;width:790px;height:869px;background:var(--content-bg);overflow:hidden}
.site-header{height:116px;background:var(--header-bg);position:relative}
.brand{position:absolute;left:24px;top:28px;display:flex;align-items:center;gap:12px}
.brand-mark{width:52px;height:52px;border-radius:50%;background:#3f8fd0}
.brand-name{font-size:38px;font-weight:700;color:#3f5a7a;line-height:1}
.brand-tagline{font-size:12px;color:#5f6b78;margin-top:4px}
.auth-links{position:absolute;right:236px;top:4px;font-size:14px;color:var(--link);word-spacing:10px}
.auth-links a{color:var(--link);text-decoration:none;margin-left:10px}
.user-card{position:absolute;right:0;top:22px;width:176px;height:94px;background:var(--user-bg);display:flex;align-items:center;padding-left:22px;gap:12px}
.user-name{font-size:12px;color:#222;margin-bottom:10px}
.user-links a{display:block;font-size:12px;color:var(--link);text-decoration:none;line-height:1.2}
.layout{display:flex;height:753px}
.sidebar{width:168px;background:var(--sidebar-bg);padding-top:24px}
.nav-item{display:flex;align-items:center;gap:16px;height:40px;padding-left:22px;color:var(--nav-text);font-size:16px}
.nav-item svg{width:26px;height:26px;flex:none}
.nav-item.is-active{color:var(--nav-active)}
.content{flex:1;padding:12px 20px 0;text-align:center}
.page-title{font-size:26px;color:var(--title);font-weight:400;margin-bottom:10px}
.tabs{display:flex;justify-content:center;gap:15px;margin-bottom:14px}
.pill{width:127px;height:34px;border-radius:17px;background:var(--pill);color:#fff;font-size:15px;line-height:34px;box-shadow:0 3px 0 var(--pill-shadow)}
.section-title{font-size:20px;color:var(--green-title);font-weight:400;margin-bottom:10px}
.plan-types{display:flex;justify-content:center;gap:26px;margin-bottom:14px}
.plan-type{width:60px;font-size:15px;color:#555}
.plan-type svg{width:60px;height:60px;display:block;margin-bottom:4px}
.divider{height:11px;background:var(--divider);margin:0 -8px 14px}
.have-title{font-size:18px;color:#444;margin-bottom:10px}
.stats{display:flex;justify-content:center;gap:24px;margin-bottom:14px}
.stat{width:120px;height:52px;background:var(--stat);color:var(--stat-text);font-size:16px;line-height:1.1;padding-top:6px}
.stat b{display:block;font-size:20px;font-weight:400}
.active-bar{height:28px;background:var(--active-bar);color:#fff;font-size:16px;line-height:28px;margin-bottom:6px}
.plan-row{display:flex;align-items:center;text-align:left;height:68px;border-bottom:1px solid #c9cbd2;padding-left:14px}
.plan-badge{width:56px;flex:none}
.plan-name{font-size:18px;margin-bottom:6px}
.plan-meta{font-size:13px;word-spacing:2px}
.plan-meta span{margin-right:22px}
.plan-row.live .plan-name,.plan-row.live .plan-meta{color:var(--plan-live)}
.plan-row .plan-name{color:var(--plan)}
.plan-row .plan-meta{color:#444}
</style>
</head>
<body>
<div class="app">
  <header class="site-header">
    <div class="brand">
      <span class="brand-mark"></span>
      <div>
        <div class="brand-name">Brellomar</div>
        <div class="brand-tagline">The most trusted resource for life management</div>
      </div>
    </div>
    <div class="auth-links"><a href="#">Sign up?</a><a href="#">Sign in</a></div>
    <div class="user-card">
      <svg width="50" height="50" viewBox="0 0 50 50" aria-hidden="true"><circle cx="25" cy="25" r="24" fill="#fff" stroke="#111" stroke-width="2"/><circle cx="25" cy="19" r="9" fill="#111"/><path d="M9 42c3-10 29-10 32 0a23 23 0 0 1-32 0z" fill="#111"/></svg>
      <div>
        <div class="user-name">Dana Voss</div>
        <div class="user-links"><a href="#">View Account</a><a href="#">Logout</a></div>
      </div>
    </div>
  </header>
  <div class="layout">
    <nav class="sidebar">
      <div class="nav-item"><svg viewBox="0 0 26 26"><path d="M2 13L13 3l11 10h-3v10h-6v-7h-4v7H5V13z" fill="#fff"/></svg>Home</div>
      <div class="nav-item"><svg viewBox="0 0 26 26"><rect x="3" y="3" width="9" height="9" fill="#fff"/><rect x="14" y="8" width="9" height="9" fill="#fff"/><rect x="5" y="14" width="9" height="9" fill="#fff"/></svg>Plans</div>
      <div class="nav-item"><svg viewBox="0 0 26 26"><path d="M6 2h10l5 5v17H6z" fill="none" stroke="#fff" stroke-width="2"/><path d="M9 11h9M9 15h9M9 19h9" stroke="#fff" stroke-width="1.5"/></svg>Documents</div>
      <div class="nav-item"><svg viewBox="0 0 26 26"><rect x="2" y="6" width="22" height="15" fill="none" stroke="#fff" stroke-width="2"/><path d="M2 6l11 9 11-9" fill="none" stroke="#fff" stroke-width="2"/></svg>Messages</div>
      <div class="nav-item"><svg viewBox="0 0 26 26"><circle cx="10" cy="9" r="5" fill="none" stroke="#fff" stroke-width="2"/><path d="M2 23c1-7 15-7 16 0" fill="none" stroke="#fff" stroke-width="2"/><circle cx="18" cy="8" r="4" fill="none" stroke="#fff" stroke-width="1.5"/></svg>Comments</div>
      <div class="nav-item is-active"><svg viewBox="0 0 26 26"><path d="M13 6a6 6 0 0 0-4 10.5V19h8v-2.5A6 6 0 0 0 13 6z" fill="none" stroke="#fff" stroke-width="1.5"/><path d="M10 22h6M13 1v2M3 10h2M21 10h2M5 3l2 2M21 3l-2 2" stroke="#fff" stroke-width="1.5"/></svg>Learning</div>
      <div class="nav-item"><svg viewBox="0 0 26 26"><circle cx="13" cy="13" r="10" fill="#3f8fd0"/></svg>Community</div>
    </nav>
    <main class="content">
      <h1 class="page-title">Learning Center</h1>
      <div class="tabs">
        <div class="pill">Get Started</div><div class="pill">Tutorials</div><div class="pill">FAQ</div><div class="pill">Templates</div>
      </div>
      <h2 class="section-title">Recommended Plans</h2>
      <div class="plan-types">
        <div class="plan-type"><svg viewBox="0 0 60 60"><circle cx="30" cy="30" r="28" fill="var(--icon-fill)" stroke="var(--icon-line)" stroke-width="2"/><g fill="var(--icon-line)"><circle cx="20" cy="20" r="4"/><circle cx="40" cy="20" r="4"/><circle cx="30" cy="25" r="3"/><rect x="16" y="26" width="8" height="18" rx="2"/><rect x="36" y="26" width="8" height="18" rx="2"/><rect x="27" y="30" width="6" height="12" rx="2"/></g></svg>Life</div>
        <div class="plan-type"><svg viewBox="0 0 60 60"><circle cx="30" cy="30" r="28" fill="var(--icon-fill)" stroke="var(--icon-line)" stroke-width="2"/><g stroke="var(--icon-line)" stroke-width="3" fill="none" stroke-linecap="round"><path d="M16 40l10-8 8 6 8-14"/><path d="M18 22l8 4"/><path d="M12 46h36"/></g><circle cx="40" cy="18" r="4" fill="var(--icon-line)"/></svg>Accident</div>
        <div class="plan-type"><svg viewBox="0 0 60 60"><circle cx="30" cy="30" r="28" fill="var(--icon-fill)" stroke="var(--icon-line)" stroke-width="2"/><path d="M14 30l16-14 16 14h-4v14H18V30z" fill="none" stroke="var(--icon-line)" stroke-width="3"/><rect x="26" y="34" width="8" height="10" fill="var(--icon-line)"/></svg>Home</div>
        <div class="plan-type"><svg viewBox="0 0 60 60"><circle cx="30" cy="30" r="28" fill="var(--icon-fill)" stroke="var(--icon-line)" stroke-width="2"/><path d="M14 36v-6l5-10h22l5 10v6z" fill="none" stroke="var(--icon-line)" stroke-width="3"/><circle cx="20" cy="38" r="4" fill="var(--icon-line)"/><circle cx="40" cy="38" r="4" fill="var(--icon-line)"/></svg>Auto</div>
        <div class="plan-type"><svg viewBox="0 0 60 60"><circle cx="30" cy="30" r="28" fill="var(--icon-fill)" stroke="var(--icon-line)" stroke-width="2"/><rect x="20" y="14" width="20" height="32" rx="3" fill="none" stroke="var(--icon-line)" stroke-width="3"/><path d="M26 14v-4h8v4M20 24h20" stroke="var(--icon-line)" stroke-width="2" fill="none"/></svg>Travel</div>
        <div class="plan-type"><svg viewBox="0 0 60 60"><circle cx="30" cy="30" r="28" fill="var(--icon-fill)" stroke="var(--icon-line)" stroke-width="2"/><path d="M30 14v32M14 30h32" stroke="var(--icon-line)" stroke-width="4"/></svg>More</div>
      </div>
      <div class="divider"></div>
      <div class="have-title">You have:</div>
      <div class="stats">
        <div class="stat"><b>4</b>Plans</div><div class="stat"><b>12</b>Contacts</div><div class="stat"><b>8</b>Documents</div><div class="stat"><b>12</b>Messages</div>
      </div>
      <div class="active-bar">Active Plans</div>
      <div class="plan-row live">
        <div class="plan-badge"><svg width="40" height="40" viewBox="0 0 40 40"><path d="M20 1l19 19-19 19L1 20z" fill="var(--end)"/><text x="20" y="24" text-anchor="middle" font-size="10" fill="#fff" font-family="Arimo,sans-serif">END</text></svg></div>
        <div><div class="plan-name">Outdoor Adventure - LIVE</div><div class="plan-meta"><span>Start: 7/01/2015</span><span>End: 7/05/2015</span><span>Groups: 2</span><span>Documents: 0</span><span>Contacts: 4</span></div></div>
      </div>
      <div class="plan-row">
        <div class="plan-badge"></div>
        <div><div class="plan-name">Mira A Birthday</div><div class="plan-meta"><span>Start: 9/09/2015</span><span>End: 9/09/2015</span><span>Documents: 0</span><span>Contacts: 1</span></div></div>
      </div>
      <div class="plan-row">
        <div class="plan-badge"></div>
        <div><div class="plan-name">Maui Vacation</div><div class="plan-meta"><span>Start: 10/09/2015</span><span>End: 10/16/2015</span><span>Documents: 3</span><span>Contacts: 8</span></div></div>
      </div>
      <div class="plan-row">
        <div class="plan-badge"><svg width="40" height="40" viewBox="0 0 40 40"><path d="M20 1l19 19-19 19L1 20z" fill="var(--start)"/><text x="20" y="24" text-anchor="middle" font-size="9" fill="#fff" font-family="Arimo,sans-serif">START</text></svg></div>
        <div><div class="plan-name">Having a Baby</div></div>
      </div>
    </main>
  </div>
</div>
</body>
</html>
```